Book Cover for Willow Kindred Notes from the Meadow

We have written a book that brings together Notes from the Meadow from a variety of women's voices.
We developed a draft book cover that we like using Canva (attached below). We'd love a book cover that is similar to this image, but looks more professional.
Following are the themes we’d like to depict in the book cover, and in parentheses, how they are represented in the current cover:
1. Divinely feminine (overall cover)
2. Currents of enlightenment (the swirls of light carrying the butterfly)
3. Diversity (a myriad of colors)
4. The solo journey into the unknown (the single butterfly’s flight)
5. Buoyancy and joy (again, the dancing colors and floating butterfly)
6. Boldly feminine (the blue butterfly, set against brush strokes of light)
7. Homage to a dear friend (she loved blue butterflies, the cosmos - this butterfly has hints of the cosmos in her wings, and painting - this background has brush strokes of light).
Book Title, Subtitle, and Editor:
Willow Kindred
Notes from the Meadow
Edited by Mirela Tove
Thank you very much for considering this project!
People who are interested in Women and Spirituality

```html
<!DOCTYPE html>
<html lang="en">
<head>
<meta charset="utf-8">
<title>Willow Kindred – Book Cover</title>
<link rel="stylesheet" href="https://fonts.googleapis.com/css2?family=Bodoni+Moda:wght@500&family=Allura&family=Montserrat:wght@400&display=swap">
<style>
  :root {
    --stage: #68696b;
    --title-blue: #27389a;
    --ink: #111114;
    --sky: #3fc4ee;
    --lemon: #f1f06a;
    --blush: #f4a9c6;
    --rose: #ec4f7a;
    --lilac: #c8b4e4;
    --wing-deep: #1c3f9e;
    --wing-bright: #2aa8e8;
  }
  html, body {
    margin: 0;
    width: 1200px;
    height: 1200px;
    overflow: hidden;
    background: var(--stage);
  }
  .cover {
    position: absolute;
    left: 360px;
    top: 240px;
    width: 480px;
    height: 720px;
    overflow: hidden;
    background:
      radial-gradient(ellipse 55% 40% at 85% 25%, var(--lemon) 0%, rgba(241,240,106,0) 100%),
      radial-gradient(ellipse 60% 45% at 10% 20%, var(--sky) 0%, rgba(63,196,238,0) 100%),
      radial-gradient(ellipse 50% 35% at 20% 70%, var(--sky) 0%, rgba(63,196,238,0) 100%),
      radial-gradient(ellipse 45% 30% at 50% 55%, #f6f0ff 0%, rgba(246,240,255,0) 100%),
      radial-gradient(ellipse 55% 25% at 75% 92%, var(--rose) 0%, rgba(236,79,122,0) 100%),
      radial-gradient(ellipse 60% 30% at 20% 98%, var(--blush) 0%, rgba(244,169,198,0) 100%),
      linear-gradient(160deg, #8fd9f2 0%, #c9eef0 35%, var(--lilac) 70%, #f6c9d9 100%);
  }
  .title {
    position: absolute;
    left: 0;
    top: 0;
    margin: 0;
    font-family: "Bodoni Moda", "Didot", serif;
    font-weight: 500;
    font-size: 82px;
    line-height: 1;
    color: var(--title-blue);
  }
  .title span { position: absolute; white-space: nowrap; }
  .title .line-one { left: 60px; top: 76px; }
  .title .line-two { left: 112px; top: 161px; }
  .butterfly {
    position: absolute;
    left: 164px;
    top: 271px;
    width: 170px;
    height: 235px;
    border-radius: 60% 40% 45% 55% / 45% 30% 70% 55%;
    background: radial-gradient(circle at 45% 45%, var(--wing-bright) 0%, #1e6fd0 55%, var(--wing-deep) 100%);
  }
  .subtitle {
    position: absolute;
    left: 0;
    width: 480px;
    top: 553px;
    margin: 0;
    text-align: center;
    font-family: "Allura", cursive;
    font-weight: 400;
    font-size: 42px;
    line-height: 1;
    color: var(--ink);
    white-space: nowrap;
  }
  .editor {
    position: absolute;
    right: 31px;
    top: 673px;
    margin: 0;
    font-family: "Montserrat", sans-serif;
    font-size: 18.5px;
    line-height: 1;
    color: var(--ink);
    white-space: nowrap;
  }
</style>
</head>
<body>
  <main class="cover">
    <h1 class="title"><span class="line-one">Willow</span><span class="line-two">Kindred</span></h1>
    <div class="butterfly" role="img" aria-label="Illustration of a single blue butterfly with starry, cosmic speckled wings in flight"></div>
    <p class="subtitle">Notes from the Meadow</p>
    <p class="editor">Edited by Mirela Tove</p>
  </main>
</body>
</html>
```